Life Insurance Landing Page (for lead gen)

We need a high converting life insurance page created. It will be housed at www.CoverCheckpoint.com. We will be driving former life insurance prospects to this page where they will only need to confirm their phone number & email in order to receive an updated quote.
Updates

Only the page design is required, the coding will be done on our end. 

Target Market(s)

People who have expressed an interest in obtaining life insurance.

Industry/Entity Type

Life Insurance

Requirements
Must have
• 1) Under "CoverCheckpoint.com" Please include a "Powered by TPVN" tag and match the colors of this site: http://thetpvn.com/life-insurance-services.html to the page.

2) The form should ask for their phone number and include an appointment calendar widget (we'll code the functionality) so they can choose the date/time of their call. It should also have an email confirmation field.

3) the overall message next to the form fields should be "Thanks for visiting Gordon (we'll personalize this "firstname" field ), please let us know the best time to schedule a brief call so we can give you an updated, rock bottom pricing quote on a policy. We'll also email you with the information, please confirm your email here and we'll send you the details.

4) We'd like to include a box that appears to be a personalized "quote briefing" snapshot that will list this information: "Name: _________" "Birth Date:"____________" "Policy Type: _______", "Coverage Amount: ____________" " all these fields will be populated into the page.

```html
<!DOCTYPE html>
<html lang="en">
<head>
<meta charset="utf-8">
<title>CoverCheckpoint.com – Life Insurance Quote</title>
<link href="https://fonts.googleapis.com/css2?family=Lato:wght@400;700;900&family=Archivo+Black&family=Arimo:wght@400;700&display=swap" rel="stylesheet">
<style>
:root{
  --blue:#1a8fd0;
  --blue-dark:#0c6aa8;
  --blue-deep:#0f6aa6;
  --red:#c4161c;
  --dark-red:#9b0f12;
  --ink:#2b2b2b;
  --text:#333;
  --field:#efefef;
  --field-line:#c9c9c9;
  --page:#ffffff;
}
*{box-sizing:border-box;margin:0;padding:0}
html,body{width:1174px;height:1200px;overflow:hidden;background:var(--page)}
body{position:relative;font-family:'Lato',sans-serif;color:var(--text)}
.abs{position:absolute}

/* top bar & hero */
.top-bar{left:0;top:0;width:1174px;height:54px;background:linear-gradient(#1b9ad9,#117fc2)}
.hero{left:0;top:54px;width:1174px;height:459px;
  background:linear-gradient(100deg,#eef1f2 0%,#d8dadb 30%,#c9c4bd 55%,#e4e2dc 75%,#d7dd9c 92%,#c8d25a 100%)}
.follow{left:139px;top:14px;display:flex;align-items:center;gap:7px;color:#fff;font-family:'Arimo',sans-serif;font-size:22px}
.follow .label{margin-right:3px}
.social{width:26px;height:26px;border-radius:50%;background:#fff;display:inline-block}

.brand{left:415px;top:0;width:344px;height:112px}
.brand-name{left:415px;top:12px;width:344px;text-align:center;font-weight:700;font-size:38px;color:var(--blue-dark);letter-spacing:-0.5px}
.brand-com{left:700px;top:56px;font-size:17px;color:#222}
.powered{left:415px;top:77px;width:344px;text-align:center;font-weight:700;font-size:15px;color:var(--dark-red)}

.headline{left:144px;top:180px;font-family:'Archivo Black',sans-serif;font-size:35px;color:var(--ink);letter-spacing:-0.5px}
.intro{left:144px;top:230px;width:440px;font-size:19px;line-height:25px;color:#2c2c2c}
.signature{left:144px;top:378px;width:135px;height:30px;background:linear-gradient(90deg,rgba(40,40,40,.35),rgba(40,40,40,.15));border-radius:4px}
.role{left:144px;top:406px;font-size:22px;color:#222}
.company{left:144px;top:434px;font-size:15.5px;color:#333}
.dots{left:973px;top:490px;display:flex;gap:7px}
.dots span{width:12px;height:12px;border-radius:50%;background:var(--blue-dark)}
.dots span:first-child{background:var(--dark-red)}

/* appointment form */
.form-panel{left:669px;top:104px;width:366px;height:286px;background:#fff;border:1px solid #ddd;box-shadow:0 0 6px rgba(0,0,0,.25)}
.form-head{left:672px;top:107px;width:361px;height:46px;background:linear-gradient(#1b9ad9,#117fc2);color:#fff;font-size:29px;font-weight:700;text-align:center;line-height:46px}
.field{background:var(--field);border:1px solid var(--field-line);border-radius:3px;font-size:13px;color:#555;padding-left:10px;display:flex;align-items:center}
.icon{position:absolute;right:9px;top:50%;transform:translateY(-50%)}
.btn-quote{left:807px;top:347px;width:109px;height:30px;background:linear-gradient(#e2262b,#b30f14);border-radius:3px;color:#fff;font-weight:700;font-size:16px;text-align:right;padding-right:12px;line-height:30px}

/* calendar */
.calendar{left:637px;top:318px;width:243px;height:175px;background:#fff;border:1px solid #ccc;box-shadow:0 2px 6px rgba(0,0,0,.25);font-family:'Lato',sans-serif}
.cal-caret{left:788px;top:311px;width:12px;height:12px;background:#fff;border-left:1px solid #ccc;border-top:1px solid #ccc;transform:rotate(45deg)}
.cal-title{position:absolute;left:0;top:10px;width:100%;text-align:center;color:var(--dark-red);font-size:14px;font-weight:700}
.cal-nav{position:absolute;top:10px;width:18px;height:16px;border:1px solid #bbb;border-radius:2px}
.cal-grid{position:absolute;left:9px;top:34px;width:225px;border-collapse:collapse;font-size:10.5px;color:#333}
.cal-grid th{font-weight:400;font-size:9.5px;height:20px}
.cal-grid td{text-align:center;height:22px;border-bottom:1px solid #e3e3e3}
.cal-grid .hl{color:var(--red)}

/* content panels */
.panel{background:#fff;box-shadow:0 0 4px rgba(0,0,0,.18)}
.panel-head{background:linear-gradient(#1b9ad9,#117fc2);color:#fff;font-size:24px;font-weight:700;text-align:center}
.pfield{background:var(--field);border:1px solid var(--field-line);border-radius:2px;font-family:'Arimo',sans-serif;font-size:13px;color:#222;padding-left:12px;display:flex;align-items:center}
.ptext{font-family:'Arimo',sans-serif;font-size:13px;line-height:19px;color:#222;padding:10px 12px;align-items:flex-start}
.why-text{left:148px;top:779px;width:878px;text-align:center;font-family:'Arimo',sans-serif;font-size:13px;line-height:19.3px;color:#222}
.read-more{left:138px;top:838px;width:898px;text-align:center;font-family:'Arimo',sans-serif;font-weight:700;font-size:13.5px;color:var(--blue-dark)}

.rule{height:1px;background:#ddd}
.commit-title{left:138px;top:914px;width:898px;text-align:center;font-size:24px;font-weight:700;color:var(--blue-dark)}
.commit-lead{left:138px;top:961px;width:898px;text-align:center;font-size:13.5px;font-weight:700;color:#222}
.commit-body{left:138px;top:986px;width:898px;text-align:center;font-size:13px;line-height:19.3px;color:#333}

/* footer */
.footer{left:0;top:1089px;width:1174px;height:111px;background:var(--blue-deep)}
.foot-links{left:138px;top:1106px;color:#fff;font-size:13.5px;font-weight:700}
.foot-links span{margin:0 6px;font-weight:400}
.foot-follow{left:135px;top:1134px;display:flex;align-items:center;gap:8px;color:#fff;font-family:'Arimo',sans-serif;font-size:22px}
.copyright{left:138px;top:1172px;color:#fff;font-size:13.5px;letter-spacing:.3px}
.disc-title{left:543px;top:1099px;color:#fff;font-size:19px;font-weight:700}
.disc-rule{left:543px;top:1128px;width:494px;height:1px;background:#3c93cc}
.disc-text{left:543px;top:1136px;width:494px;color:#fff;font-size:12.5px;line-height:15.6px;letter-spacing:.3px}
</style>
</head>
<body>

<div class="abs top-bar"></div>
<div class="abs hero" role="img" aria-label="Blurred photo of business people meeting in a bright office"></div>

<div class="abs follow"><span class="label">Follow Us</span><span class="social"></span><span class="social"></span><span class="social"></span><span class="social"></span></div>

<svg class="abs brand" viewBox="0 0 344 112" aria-hidden="true">
  <path d="M1 0 V82 L172 110 L343 82 V0 Z" fill="#fff" stroke="#d0d0d0"/>
</svg>
<div class="abs brand-name">CoverCheckpoint</div>
<div class="abs brand-com">.com</div>
<div class="abs powered">Powered by TPVN</div>

<h1 class="abs headline">Thanks for visiting Gordon</h1>
<p class="abs intro">Below is your policy summary, if you'll just confirm your contact info and pick a time that works for you I'd like to setup a really quick call just to go over a few details and give you some great pricing options I've located. Thanks again Gordon</p>
<div class="abs signature" role="img" aria-label="Handwritten signature of Daniel Hartwell III"></div>
<div class="abs role">President</div>
<div class="abs company">Trusted Partners Value Network</div>
<div class="abs dots"><span></span><span></span><span></span></div>

<!-- appointment form -->
<div class="abs form-panel"></div>
<div class="abs form-head">Phone Appointment</div>
<div class="abs field" style="left:682px;top:166px;width:339px;height:32px">Phone Number</div>
<div class="abs field" style="left:682px;top:211px;width:339px;height:32px">Appointment
  <svg class="icon" width="18" height="18" viewBox="0 0 18 18"><rect x="1" y="3" width="16" height="14" fill="none" stroke="#444" stroke-width="1.5"/><rect x="1" y="3" width="16" height="3" fill="#444"/><g fill="#444"><rect x="4" y="8" width="2" height="2"/><rect x="8" y="8" width="2" height="2"/><rect x="12" y="8" width="2" height="2"/><rect x="4" y="12" width="2" height="2"/><rect x="8" y="12" width="2" height="2"/><rect x="12" y="12" width="2" height="2"/></g></svg>
</div>
<div class="abs field" style="left:682px;top:255px;width:339px;height:32px">Email Address</div>
<div class="abs field" style="left:682px;top:293px;width:154px;height:33px">Date
  <svg class="icon" width="18" height="18" viewBox="0 0 18 18"><rect x="1" y="3" width="16" height="14" fill="none" stroke="#444" stroke-width="1.5"/><rect x="1" y="3" width="16" height="3" fill="#444"/><g fill="#444"><rect x="4" y="8" width="2" height="2"/><rect x="8" y="8" width="2" height="2"/><rect x="12" y="8" width="2" height="2"/><rect x="4" y="12" width="2" height="2"/><rect x="8" y="12" width="2" height="2"/><rect x="12" y="12" width="2" height="2"/></g></svg>
</div>
<div class="abs field" style="left:865px;top:293px;width:154px;height:33px">Time
  <svg class="icon" width="20" height="20" viewBox="0 0 20 20"><circle cx="10" cy="11" r="7.5" fill="none" stroke="#333" stroke-width="2"/><rect x="8" y="0.5" width="4" height="2.5" fill="#333"/><path d="M10 11 V6.5 M10 11 L13 13" stroke="#333" stroke-width="1.8" fill="none"/></svg>
</div>
<div class="abs btn-quote">Get Quote</div>

<!-- calendar -->
<div class="abs cal-caret"></div>
<div class="abs calendar">
  <span class="cal-nav" style="left:9px"><svg width="16" height="14" viewBox="0 0 16 14"><path d="M12 7H4M7 4L4 7L7 10" stroke="#444" fill="none" stroke-width="1.3"/></svg></span>
  <div class="cal-title">February 2014</div>
  <span class="cal-nav" style="right:9px"><svg width="16" height="14" viewBox="0 0 16 14"><path d="M4 7H12M9 4L12 7L9 10" stroke="#444" fill="none" stroke-width="1.3"/></svg></span>
  <table class="cal-grid">
    <tr><th>SUN</th><th>MON</th><th>TUE</th><th>WED</th><th>THU</th><th>FRI</th><th>SAT</th></tr>
    <tr><td></td><td></td><td></td><td></td><td></td><td></td><td>1</td></tr>
    <tr><td>2</td><td>3</td><td>4</td><td>5</td><td>6</td><td class="hl">7</td><td>8</td></tr>
    <tr><td>9</td><td>10</td><td>10</td><td>12</td><td>13</td><td>14</td><td>15</td></tr>
    <tr><td>16</td><td>17</td><td>18</td><td>19</td><td>20</td><td>21</td><td>22</td></tr>
    <tr><td>23</td><td>24</td><td>25</td><td>26</td><td>27</td><td>28</td><td></td></tr>
  </table>
</div>

<!-- policy summary -->
<section class="abs panel" style="left:138px;top:526px;width:898px;height:187px"></section>
<div class="abs panel-head" style="left:138px;top:526px;width:898px;height:47px;line-height:47px">Policy Summary</div>
<div class="abs pfield" style="left:147px;top:588px;width:300px;height:31px">Lorem ipsum dol</div>
<div class="abs pfield" style="left:455px;top:588px;width:301px;height:31px">Lorem ipsum dol</div>
<div class="abs pfield" style="left:762px;top:588px;width:264px;height:31px;padding-left:30px">$25.000
  <svg class="icon" style="right:0;width:28px;height:29px" viewBox="0 0 28 29"><rect width="28" height="29" fill="#d4d4d4"/><path d="M8 12H20L14 18Z" fill="#666"/></svg>
</div>
<div class="abs pfield ptext" style="left:147px;top:625px;width:500px;height:80px">Lorem ipsum dolor sit amet, consectetur adipisicing elit, sed do eiusmod tempor incididunt ut labore et dolore magna aliqua. Ut enim ad minim veniam, quis nostrud laboris nisi ut aliquip ex ea commodo consequat.</div>
<div class="abs pfield" style="left:657px;top:634px;width:164px;height:32px">Gordon</div>
<div class="abs pfield" style="left:829px;top:634px;width:197px;height:32px">06/04/1980
  <svg class="icon" width="18" height="18" viewBox="0 0 18 18"><rect x="1" y="3" width="16" height="14" fill="none" stroke="#555" stroke-width="1.5"/><rect x="1" y="3" width="16" height="3" fill="#555"/><g fill="#555"><rect x="4" y="8" width="2" height="2"/><rect x="8" y="8" width="2" height="2"/><rect x="12" y="8" width="2" height="2"/><rect x="4" y="12" width="2" height="2"/><rect x="8" y="12" width="2" height="2"/><rect x="12" y="12" width="2" height="2"/></g></svg>
</div>
<div class="abs pfield" style="left:657px;top:672px;width:164px;height:32px">Ut enim ad minim</div>
<div class="abs pfield" style="left:829px;top:672px;width:197px;height:32px">345 6578</div>

<!-- why life insurance -->
<section class="abs panel" style="left:138px;top:725px;width:898px;height:140px"></section>
<div class="abs panel-head" style="left:138px;top:725px;width:898px;height:47px;line-height:47px">Why Life Insurance</div>
<p class="abs why-text">Having the right life insurance is pivotal in planning for the future of you and your loved ones. Life insurance can help solve a lot of the problems your family would be faced with should the unexpected happen. Don't leave the future of you and your loved ones to chance. Trusted Partners Value Network can help you find the right life insurance coverage for you, and help ensure that your policy continually meets your needs.</p>
<div class="abs read-more">Read More »</div>

<!-- commitment -->
<div class="abs rule" style="left:165px;top:900px;width:844px"></div>
<h2 class="abs commit-title">Our Commitment</h2>
<div class="abs rule" style="left:138px;top:948px;width:898px"></div>
<p class="abs commit-lead">We Stand Behind Our Commitment to do our Best to get You the Lowest Rates Online. Getting a cheap car insurance quote is so easy now.</p>
<p class="abs commit-body">We believe in providing exceptional customer service. At Cover Checkpoint, we believe in having the best of both worlds. Low rates, excellent coverage and local reps that are there every step of the way. This is what sets Cover Checkpoint apart from our competition. And that's what makes us the obvious choice when it comes to your car insurance needs.</p>
<div class="abs rule" style="left:165px;top:1056px;width:844px"></div>

<!-- footer -->
<footer class="abs footer"></footer>
<nav class="abs foot-links">Contact Us<span>|</span>Privacy &amp; Security<span>|</span>Terms of Use<span>|</span>Opt-out</nav>
<div class="abs foot-follow"><span>Follow Us :</span><span class="social"></span><span class="social"></span><span class="social"></span><span class="social"></span></div>
<div class="abs copyright">Copyright 2014 Cover Checkpoint.</div>
<div class="abs disc-title">Disclaimer</div>
<div class="abs disc-rule"></div>
<p class="abs disc-text">Lorem ipsum dolor sit amet, consectetur adipisicing elit, sed do eiusmod tempor incididunt ut labore et dolore magna aliqua. Ut enim ad minim veniam, quis nostrud laboris nisi ut aliquip ex ea commodo consequat.</p>

</body>
</html>
```